Business Profile Landing Page for search engine Start UP " Ember Gate"

Hi there
Ember Gate is an search engine for the Ember Gate - business.

What i´m looking for is a stunning singel Profile Landing Page for the Companys presentation.

Following Details should be included.

1st section
Comapanys name
Adress
info row ( opening time or what ever)
Profile Picture Big ( Could be the logo)
+3 smaller Pictures ( Maybe the store, main product ...)

2nd Section
navigation Icons for:
Call, Mail , Web, Route, Data

3er Section
About us.

Text lines.....
+Pictures slider

4th Section
1 row : Products ( Titel , Picture, Price)
2nd row :Service ( same as Products + text lines )

5th section
Blog Posts row

.....................................................
Well thats all, Colors used from the logo, u can also use the favicon somewhere (the crown magnifying glass)

Target Market(s)

All Comapnys, it should be an " used for all" design

Number of Pages Required

1 page

Requirements
Must have
• The first sighting is the important part, so the " first section should be impressively and makes the customers curious about more informations (very important for mobile version)
Nice to have
• If you can insert our favicon somewhere would be cool, but its not nessesery
Should not have
• you dont need to make a header or footer, that part is already done. i just need the main section design

```html
<!DOCTYPE html>
<html lang="en">
<head>
<meta charset="utf-8">
<title>Ember Gate – Business Profile</title>
<link rel="stylesheet" href="https://fonts.googleapis.com/css2?family=Montserrat:wght@400;500;700;800&family=Roboto:wght@400;500;700&family=Source+Sans+3:wght@400;600&display=swap">
<style>
:root{
  --gold:#db9800;
  --gold-dark:#b97a00;
  --ink:#111111;
  --text:#555555;
  --hero-bg:#f7f7f7;
  --soft:#f2f2f2;
  --blog-bg:#f1f2f4;
  --white:#ffffff;
}
*{box-sizing:border-box;margin:0;padding:0}
html,body{width:1200px;height:2695px;overflow:hidden}
body{position:relative;background:var(--white);font-family:"Roboto",sans-serif;color:var(--text)}
.abs{position:absolute}

/* hero */
.hero{left:0;top:0;width:1200px;height:448px;background:var(--hero-bg)}
.brand-mark{left:262px;top:52px;width:270px;height:330px;display:flex;flex-direction:column;align-items:center;justify-content:center;gap:26px}
.brand-mark .ring{width:190px;height:190px;border-radius:50%;border:30px solid var(--gold)}
.brand-mark .name{font-family:"Montserrat",sans-serif;font-weight:700;font-size:38px;color:var(--gold);line-height:1}
.brand-title{left:545px;top:56px;font-family:"Montserrat",sans-serif;font-weight:700;font-size:42px;color:var(--gold);line-height:1}
.brand-rule{left:545px;top:103px;width:250px;height:2px;background:var(--gold)}
.brand-sub{left:542px;top:108px;font-family:"Montserrat",sans-serif;font-weight:400;font-size:29px;color:var(--ink)}
.info-head{display:flex;align-items:center;gap:8px;font-size:15px;color:var(--ink)}
.info-text{font-size:10px;line-height:16px;color:var(--text);width:300px}
.thumb{top:282px;width:119px;height:77px}

/* actions */
.actions{left:0;top:448px;width:1200px;height:218px;background:var(--gold)}
.action{top:52px;width:100px;display:flex;flex-direction:column;align-items:center}
.action .ring{width:82px;height:82px;border-radius:50%;border:2px solid var(--white);display:flex;align-items:center;justify-content:center}
.action .ring.dark{background:var(--ink)}
.action span{margin-top:18px;font-family:"Montserrat",sans-serif;font-weight:700;font-size:14px;color:var(--white)}

/* about */
.about{left:0;top:666px;width:577px;height:442px;background:#f9f9f9}
.about-photo{left:577px;top:666px;width:623px;height:442px;
  background:radial-gradient(ellipse 48% 42% at 52% 66%,#f4efe6 0%,rgba(226,224,220,.6) 50%,rgba(200,202,207,0) 100%),
             linear-gradient(180deg,#1f5ea8 0%,#6f8fb8 10%,#b9bcc2 18%,#d2d4d8 50%,#c3c5c9 85%,#a7a9ae 100%)}
.about h2{position:absolute;left:203px;top:108px;font-family:"Montserrat",sans-serif;font-weight:800;font-size:33px;color:var(--ink)}
.rule{height:3px;width:36px;background:var(--gold)}
.about p{position:absolute;left:203px;width:330px;font-size:13px;line-height:18.5px}

/* products / service */
.section-title{left:0;width:1200px;text-align:center;font-family:"Montserrat",sans-serif;font-weight:800;font-size:33px;color:var(--ink)}
.section-sub{left:0;width:1200px;text-align:center;font-size:13px;line-height:18.5px}
.card{width:234px;height:352px}
.card .pic{height:207px}
.card .foot{height:145px;display:flex;flex-direction:column;align-items:center;padding-top:34px;font-family:"Source Sans 3",sans-serif}
.card .foot h3{font-weight:400;font-size:14.5px;color:var(--white)}
.card .foot .price{margin-top:6px;font-size:14.5px;color:var(--white)}
.card .foot .btn{margin-top:12px;height:24px;padding:0 11px;border-radius:12px;font-family:"Montserrat",sans-serif;font-weight:700;font-size:7.5px;line-height:24px;text-transform:uppercase}
.foot.gold{background:var(--gold)} .foot.black{background:var(--ink)}
.btn.on-gold{background:var(--ink);color:var(--white)}
.btn.on-black{background:var(--gold);color:var(--white)}

/* blog */
.blog{left:0;top:2279px;width:1200px;height:416px;background:var(--blog-bg)}
.blog-title{left:225px;top:44px;font-family:"Source Sans 3",sans-serif;font-weight:600;font-size:22px;color:var(--ink)}
.blog-title em{font-style:normal;color:var(--gold)}
.see-all{left:926px;top:52px;font-family:"Source Sans 3",sans-serif;font-size:14px;color:var(--ink)}
.post{top:107px;width:234px}
.post .frame{background:var(--white);padding:8px 8px 0;height:171px}
.post .img{height:131px}
.post .cap{font-family:"Source Sans 3",sans-serif;font-size:10px;color:#333;padding-top:10px;text-transform:uppercase}
.post p{margin-top:12px;font-size:8.5px;line-height:14px;color:#666;width:210px}
.post .more{margin-top:20px;display:inline-block;height:24px;padding:0 15px;border-radius:12px;font-family:"Montserrat",sans-serif;font-weight:700;font-size:7.5px;letter-spacing:1.5px;line-height:24px;color:var(--white)}
</style>
</head>
<body>

<section class="abs hero">
  <div class="abs brand-mark"><div class="ring"></div><div class="name">Ember Gate</div></div>
  <div class="abs brand-title">Ember Gate</div>
  <div class="abs brand-rule"></div>
  <div class="abs brand-sub">Floristen &amp; Gärtner</div>

  <div class="abs info-head" style="left:539px;top:156px">
    <svg width="20" height="24" viewBox="0 0 20 24"><path d="M10 1a8 8 0 0 0-8 8c0 6 8 14 8 14s8-8 8-14a8 8 0 0 0-8-8z" fill="var(--gold)"/><circle cx="10" cy="9" r="3" fill="#fff"/></svg>Address:
  </div>
  <div class="abs info-text" style="left:544px;top:184px">Lorem ipsum suit 104, Building Harbor City consectetur adipiscing elit, sed do eiusmod</div>
  <div class="abs info-head" style="left:540px;top:227px">
    <svg width="20" height="20" viewBox="0 0 20 20"><circle cx="10" cy="10" r="8.5" fill="none" stroke="var(--gold)" stroke-width="2"/><path d="M10 5v5l3 3" fill="none" stroke="var(--gold)" stroke-width="2"/></svg>Opening Time
  </div>
  <div class="abs info-text" style="left:544px;top:254px">08:00 AM - 10:00 PM Monday Saturday</div>

  <div class="abs thumb" style="left:544px;background:radial-gradient(ellipse at 50% 70%,#d9d2c4,#8a9bbd 55%,#5a6f9c)" role="img" aria-label="Store aisle with stocked shelves"></div>
  <div class="abs thumb" style="left:671px;background:radial-gradient(ellipse at 40% 40%,#d6dcea,#4f74c0 55%,#2d4c95)" role="img" aria-label="Shoppers in a supermarket aisle"></div>
  <div class="abs thumb" style="left:799px;background:linear-gradient(180deg,#4f88cf 0%,#9fb6d2 30%,#d9cfc4 60%,#b23a36 100%)" role="img" aria-label="Value Depot storefront exterior"></div>
</section>

<nav class="abs actions">
  <div class="abs action" style="left:277px"><div class="ring">
    <svg width="44" height="44" viewBox="0 0 44 44" fill="none" stroke="#fff" stroke-width="2"><circle cx="22" cy="22" r="19"/><path d="M15 13l4 0 2 5-3 2a12 12 0 0 0 6 6l2-3 5 2v4c-10 1-17-6-16-16z"/></svg>
  </div><span>CALL</span></div>
  <div class="abs action" style="left:413px"><div class="ring dark">
    <svg width="44" height="44" viewBox="0 0 44 44" fill="none" stroke="#fff" stroke-width="2"><rect x="4" y="10" width="30" height="22" rx="2"/><path d="M4 11l15 12 15-12"/><circle cx="34" cy="31" r="7" fill="#111"/><path d="M31 31l2 2 4-4"/></svg>
  </div><span>MAIL</span></div>
  <div class="abs action" style="left:551px"><div class="ring">
    <svg width="44" height="44" viewBox="0 0 44 44" fill="none" stroke="#fff" stroke-width="2"><circle cx="22" cy="22" r="18"/><ellipse cx="22" cy="22" rx="8" ry="18"/><path d="M4 22h36M7 13h30M7 31h30M22 4v36"/></svg>
  </div><span>WEB</span></div>
  <div class="abs action" style="left:688px"><div class="ring">
    <svg width="44" height="44" viewBox="0 0 44 44" fill="none" stroke="#fff" stroke-width="2"><circle cx="11" cy="11" r="4"/><circle cx="36" cy="33" r="3"/><path d="M15 11h15a5 5 0 0 1 0 10H14a5 5 0 0 0 0 10h14M25 28l3 3-3 3"/></svg>
  </div><span>ROUTE</span></div>
  <div class="abs action" style="left:822px"><div class="ring">
    <svg width="44" height="44" viewBox="0 0 44 44" fill="none" stroke="#fff" stroke-width="2"><path d="M14 30H11a7 7 0 0 1 0-14 10 10 0 0 1 19-3 8 8 0 0 1 3 17h-3"/><path d="M22 18v20M18 22l4-4 4 4M19 35l3 3 3-3"/></svg>
  </div><span>DATA</span></div>
</nav>

<section class="abs about">
  <h2>ABOUT US.</h2>
  <div class="abs rule" style="left:203px;top:148px"></div>
  <p style="top:166px">Lorem ipsum dolor sit amet, consectetur adipiscing elit, sed do eiusmod tempor incididunt ut labore et dolore magna aliqua. Ut enim ad minim veniam, quis nostrud exercitation ullamco laboris nisi ut aliquip ex ea commodo consequat.</p>
  <p style="top:270px">Ut enim ad minim veniam, quis nostrud exercitation ullamco laboris nisi ut aliquip ex ea commodo.</p>
</section>
<div class="abs about-photo" role="img" aria-label="Lit glass storefront of a modern retail shop under a blue sky"></div>

<h2 class="abs section-title" style="top:1175px">PRODUCTS</h2>
<div class="abs rule" style="left:582px;top:1216px"></div>
<p class="abs section-sub" style="top:1233px">Ut enim ad minim veniam, quis nostrud exercitation<br>ullamco laboris nisi ut aliquip ex ea commodo.</p>

<div class="abs card" style="left:232px;top:1316px">
  <div class="pic" style="background:radial-gradient(ellipse 34% 42% at 50% 48%,#5a1418 0%,#7a2a2e 45%,#d9cfd0 80%,#f2f2f2 100%)" role="img" aria-label="Boxed dark chocolates with red ribbon"></div>
  <div class="foot gold"><h3>DARK CHOCOLATES</h3><div class="price">$59.00</div><div class="btn on-gold">View Selection</div></div>
</div>
<div class="abs card" style="left:482px;top:1316px">
  <div class="pic" style="background:radial-gradient(ellipse 36% 40% at 50% 50%,#6e1a1f 0%,#83373a 45%,#ddd2d2 80%,#f2f2f2 100%)" role="img" aria-label="Boxed milk chocolates with red ribbon"></div>
  <div class="foot black"><h3>MILK CHOCOLATES</h3><div class="price">$19.00</div><div class="btn on-black">View Product</div></div>
</div>
<div class="abs card" style="left:733px;top:1316px">
  <div class="pic" style="background:radial-gradient(ellipse 36% 24% at 50% 45%,#3b1a0e 0%,#5a2e1c 50%,#d8cdc6 82%,#f2f2f2 100%)" role="img" aria-label="Soft centre chocolates"></div>
  <div class="foot black"><h3>SOFT CENTRES</h3><div class="price">$29.00</div><div class="btn on-black">View Selection</div></div>
</div>

<h2 class="abs section-title" style="top:1720px">SERVICE</h2>
<div class="abs rule" style="left:582px;top:1761px"></div>
<p class="abs section-sub" style="top:1778px">Ut enim ad minim veniam, quis nostrud exercitation<br>ullamco laboris nisi ut aliquip ex ea commodo.</p>

<div class="abs card" style="left:232px;top:1849px">
  <div class="pic" style="background:radial-gradient(ellipse 34% 40% at 50% 50%,#3a3a3c 0%,#8d9095 50%,#dedfe1 80%,#f2f2f2 100%)" role="img" aria-label="Electric shaver with charging stand"></div>
  <div class="foot black"><h3>DARK CHOCOLATES</h3><div class="price">$59.00</div><div class="btn on-black">View Selection</div></div>
</div>
<div class="abs card" style="left:482px;top:1849px">
  <div class="pic" style="background:radial-gradient(ellipse 36% 38% at 50% 52%,#2b3a7a 0%,#8a8fae 45%,#e6e1d8 78%,#f2f2f2 100%)" role="img" aria-label="Natural care product bottles"></div>
  <div class="foot gold"><h3>MILK CHOCOLATES</h3><div class="price">$19.00</div><div class="btn on-gold">View Product</div></div>
</div>
<div class="abs card" style="left:733px;top:1849px">
  <div class="pic" style="background:radial-gradient(ellipse 40% 32% at 50% 52%,#1d3f7a 0%,#7a3a48 40%,#d9b45a 62%,#ecebe6 82%,#f2f2f2 100%)" role="img" aria-label="Assorted packaged goods"></div>
  <div class="foot gold"><h3>SOFT CENTRES</h3><div class="price">$29.00</div><div class="btn on-gold">View Selection</div></div>
</div>

<section class="abs blog">
  <div class="abs blog-title"><em>Blog</em> Feeds</div>
  <div class="abs see-all">SEE ALL</div>

  <article class="abs post" style="left:225px">
    <div class="frame"><div class="img" style="background:linear-gradient(180deg,#5f9ad8 0%,#a9c3df 25%,#cdb49a 55%,#9b7a5e 100%)" role="img" aria-label="Department store entrance"></div><div class="cap">Complete list of stores</div></div>
    <p>Lorem ipsum dolor sit amet, consectetur adipiscing elit, sed do eiusmod tempor inci ut labore et dolore magna aliqua sit amet...</p>
    <span class="more" style="background:var(--gold)">READ MORE</span>
  </article>
  <article class="abs post" style="left:483px">
    <div class="frame"><div class="img" style="background:linear-gradient(180deg,#e3e5e8 0%,#c6c9ce 45%,#6f737b 80%,#9a9ca1 100%)" role="img" aria-label="Warehouse store entrance"></div><div class="cap">Bulkway now supports TapPay</div></div>
    <p>Lorem ipsum dolor sit amet, consectetur adipiscing elit, sed do eiusmod tempor inci ut labore et dolore magna aliqua sit amet...</p>
    <span class="more" style="background:#333">READ MORE</span>
  </article>
  <article class="abs post" style="left:741px">
    <div class="frame"><div class="img" style="background:linear-gradient(180deg,#a8c9ea 0%,#d8d6dc 22%,#c9303b 45%,#b81d28 85%,#c9b7a8 100%)" role="img" aria-label="Red toy store building"></div><div class="cap">Dollhouse store Grand Plaza Mall</div></div>
    <p>Lorem ipsum dolor sit amet, consectetur adipiscing elit, sed do eiusmod tempor inci ut labore et dolore magna aliqua sit amet...</p>
    <span class="more" style="background:#333">READ MORE</span>
  </article>
</section>

</body>
</html>
```